Partial Vehicle Wrap for Vacation Rental Company

We are purchasing new 2024 Valtor Stride Hauler vans for our maintenance team and will be wrapping the vehicles. The wrap will be a partial wrap, meaning it will only cover 50% of the vehicle, the rest will be white. Our company does property management for vacation rentals in Columbia and Lake Murray SC. We have a more modern and clean aesthetic - our website is pinecovecottagesuites.com. I have uploaded our logo as an example of our colors and brand guidelines.

Target Market(s)

Lake Vacation and Family Oriented

Industry/Entity Type

Vacation rental management

Font styles to use
Sans Serif

Colors
0054AA
0677BA
7BADD7
CADEEF
E8F1F8

Requirements
Must have
• Our company name, phone number, brand colors
Nice to have
• Clean lines, modern, easy to read
Should not have
• We don't want this to be too busy, with too much going on.

```html
<!DOCTYPE html>
<html lang="en">
<head>
<meta charset="utf-8">
<title>Pinecove Cottage Suites – Van Wrap Layout</title>
<link rel="stylesheet" href="https://fonts.googleapis.com/css2?family=Montserrat:wght@400;600&display=swap">
<style>
  :root {
    --stage: #000000;
    --vinyl-white: #e9eaec;
    --brand-blue: #0677ba;
    --brand-deep: #0054aa;
    --logo-grey: #4b5058;
    --photo-warm-a: #e3d8cb;
    --photo-warm-b: #a8927c;
    --photo-cool-a: #e6e2dc;
    --photo-cool-b: #b9b1a6;
  }
  html, body {
    margin: 0;
    padding: 0;
    width: 667px;
    height: 1200px;
    overflow: hidden;
    background: var(--stage);
  }
  .wrap-sheet { display: block; }
  .panel-base { fill: var(--vinyl-white); }
  .photo-edge { fill: none; stroke: var(--brand-blue); stroke-width: 2.5; stroke-linejoin: miter; }
  .door-seam { stroke: #c9cbcf; stroke-width: 1; }
  .brand-name {
    font-family: "Montserrat", sans-serif;
    font-weight: 600;
    fill: var(--logo-grey);
    letter-spacing: 0.14em;
  }
  .phone-number {
    font-family: "Montserrat", sans-serif;
    font-weight: 600;
    fill: var(--brand-blue);
  }
  .phone-icon { fill: var(--logo-grey); }
  .panel-caption {
    font-family: "Montserrat", sans-serif;
    font-weight: 400;
    fill: #6b7078;
    font-size: 10px;
    letter-spacing: 0.2em;
  }
</style>
</head>
<body>
<svg class="wrap-sheet" width="667" height="1200" viewBox="0 0 667 1200" xmlns="http://www.w3.org/2000/svg">
  <defs>
    <linearGradient id="interior-warm" x1="0" y1="0" x2="1" y2="1">
      <stop offset="0" stop-color="var(--photo-warm-a)"/>
      <stop offset="1" stop-color="var(--photo-warm-b)"/>
    </linearGradient>
    <linearGradient id="interior-cool" x1="0" y1="0" x2="1" y2="1">
      <stop offset="0" stop-color="var(--photo-cool-a)"/>
      <stop offset="1" stop-color="var(--photo-cool-b)"/>
    </linearGradient>
    <symbol id="phone-glyph" viewBox="0 0 24 24">
      <path d="M6.6 10.8a15.1 15.1 0 0 0 6.6 6.6l2.2-2.2a1 1 0 0 1 1-.25 11.4 11.4 0 0 0 3.6.57 1 1 0 0 1 1 1V20a1 1 0 0 1-1 1A17 17 0 0 1 3 4a1 1 0 0 1 1-1h3.5a1 1 0 0 1 1 1c0 1.25.2 2.45.57 3.57a1 1 0 0 1-.25 1z"/>
    </symbol>
  </defs>

  <!-- Driver side panel -->
  <g class="side-panel side-panel--driver" transform="translate(14 70)">
    <rect class="panel-base" width="640" height="210" rx="10"/>
    <polygon role="img" aria-label="Photo of a bright furnished living room with fireplace" fill="url(#interior-cool)" points="0,0 139,0 139,22 27,100 0,83"/>
    <polyline class="photo-edge" points="139,0 139,22 27,100 0,83"/>
    <polygon role="img" aria-label="Photo of a colourful living room with blue sofa and patterned rug" fill="url(#interior-warm)" points="0,139 102,71 218,154 218,210 0,210"/>
    <polyline class="photo-edge" points="0,139 102,71 218,154 218,210"/>
    <text class="brand-name" x="166" y="66" font-size="15">PINECOVE</text>
    <text class="brand-name" x="166" y="84" font-size="11">COTTAGE SUITES</text>
    <use href="#phone-glyph" class="phone-icon" x="229" y="178" width="12" height="12"/>
    <text class="phone-number" x="244" y="189" font-size="11.5">+1 803 555 0147</text>
  </g>

  <!-- Passenger side panel -->
  <g class="side-panel side-panel--passenger" transform="translate(14 390)">
    <rect class="panel-base" width="640" height="210" rx="10"/>
    <polygon role="img" aria-label="Photo of a living room with fireplace, shelving and sofa" fill="url(#interior-cool)" points="640,0 484,0 484,22 600,100 640,90"/>
    <polyline class="photo-edge" points="484,0 484,22 600,100 640,90"/>
    <polygon role="img" aria-label="Photo of an open living and dining room with sectional sofa" fill="url(#interior-warm)" points="640,139 530,71 395,154 395,210 640,210"/>
    <polyline class="photo-edge" points="640,139 530,71 395,154 395,210"/>
    <text class="brand-name" x="323" y="66" font-size="15">PINECOVE</text>
    <text class="brand-name" x="323" y="84" font-size="11">COTTAGE SUITES</text>
    <use href="#phone-glyph" class="phone-icon" x="280" y="178" width="12" height="12"/>
    <text class="phone-number" x="295" y="189" font-size="11.5">+1 803 555 0147</text>
  </g>

  <!-- Rear doors panel -->
  <g class="rear-panel" transform="translate(158 710)">
    <rect class="panel-base" width="350" height="260" rx="10"/>
    <line class="door-seam" x1="175" y1="0" x2="175" y2="260"/>
    <polygon role="img" aria-label="Photo of a sitting area with framed painting" fill="url(#interior-warm)" points="0,0 65,0 65,100 0,140"/>
    <polyline class="photo-edge" points="65,0 65,100 0,140"/>
    <polygon role="img" aria-label="Photo of a bedroom corner with lamp and artwork" fill="url(#interior-cool)" points="350,0 285,0 285,100 350,140"/>
    <polyline class="photo-edge" points="285,0 285,100 350,140"/>
    <polygon role="img" aria-label="Photo of a dining area with white chairs" fill="url(#interior-cool)" points="0,197 27,177 142,260 0,260"/>
    <polyline class="photo-edge" points="0,197 27,177 142,260"/>
    <polygon role="img" aria-label="Photo of a living room with blue sofa" fill="url(#interior-warm)" points="350,200 317,177 205,260 350,260"/>
    <polyline class="photo-edge" points="350,200 317,177 205,260"/>
    <text class="brand-name" x="175" y="42" font-size="13" text-anchor="middle">PINECOVE</text>
    <text class="brand-name" x="175" y="57" font-size="9.5" text-anchor="middle">COTTAGE SUITES</text>
    <use href="#phone-glyph" class="phone-icon" x="131" y="230" width="10" height="10"/>
    <text class="phone-number" x="144" y="239" font-size="9.5">+1 803 555 0147</text>
  </g>
</svg>
</body>
</html>
```